Mesa VerdaLighting and Design Web Page

We are a Sales Agency that represents 40+ LED Lighting manufacturers primarily in new commercial, industrial and architectural construction projects. We also are active in the Re-Light and Retrofit Lighting market.
Our current web page can be found at www.mesaverdalighting.example. Our local competitors are www.beaconlumenpw.example,. We would like a more dynamic website that will list our manufacturers we represent and links to their websites. Please offer suggestions to provide a more dynamic website using our new logo which is attached. Please use the color scheme from logo. The final design should communicate innovation and expertise in LED lighting.

Target Market(s)

Architects, Lighting designers, Electrical Engineers, Electrical Contractors, Electrical Distributors, Facility Engineers, Energy Engineers

Industry/Entity Type

Construction

Number of Pages Required

5+ page

Font styles to use
Other font styles liked:
• MS Reference Sans Serif, or close to our LOGO font.

Colors
f78f20
959595

Requirements
Must have
• Logo incorporated with matching background, clean professional look based on logo, links to our manufacturers web page
Nice to have
• LED Lighting project stock photos as examples
Should not have
• crowded pages with text

```html
<!DOCTYPE html>
<html lang="en">
<head>
<meta charset="utf-8">
<title>Mesa Verda Lighting – About us</title>
<link rel="stylesheet" href="https://fonts.googleapis.com/css2?family=Open+Sans:wght@400;600;700&display=swap">
<style>
:root{
  --orange:#e35720;
  --orange-soft:#f78f20;
  --grey:#959595;
  --header-bg:#ececec;
  --text:#3c3c3c;
  --footer-bg:#343434;
  --footer-text:#a9a9a9;
}
*{margin:0;padding:0;box-sizing:border-box}
html,body{width:1200px;height:835px;overflow:hidden;background:#fff}
body{font-family:"Open Sans",Arial,sans-serif;color:var(--text);position:relative}

.site-header{position:absolute;left:0;top:0;width:1200px;height:130px;background:var(--header-bg)}
.brand{position:absolute;left:104px;top:42px;display:flex;align-items:center;gap:10px}
.brand-dot{width:30px;height:30px;border-radius:50%;background:var(--orange)}
.brand-name{font-size:19px;font-weight:600;color:var(--orange);line-height:1}

.contact-bar{position:absolute;right:92px;top:22px;display:flex;align-items:center;gap:10px}
.contact-line{font-size:11px;color:var(--orange);margin-right:2px}
.social{width:26px;height:26px;background:var(--orange)}

.main-nav{position:absolute;left:498px;top:76px;display:flex}
.nav-item{width:102px;height:54px;display:flex;align-items:center;justify-content:center;font-size:12.5px;color:#8a8a8a;padding-top:2px}
.nav-item.is-active{background:var(--orange);color:#fff}

.hero-photo{position:absolute;left:0;top:130px;width:698px;height:582px;
  background:linear-gradient(120deg,#6b5a48 0%,#9c8f80 25%,#b9c6d6 45%,#8aa3bf 60%,#c7b9a2 80%,#6c6458 100%)}
.hero-title{position:absolute;left:24px;bottom:-19px;font-size:170px;font-weight:400;color:var(--orange);
  line-height:1;white-space:nowrap;transform:scaleX(0.95);transform-origin:left bottom}

.shade{position:absolute;left:698px;top:130px;width:502px;height:14px;background:linear-gradient(#d6d6d6,#fff)}

.about-copy{position:absolute;left:762px;top:177px;width:383px;font-size:15.2px;line-height:21.6px;text-align:justify;color:var(--text);letter-spacing:0.15px}
.about-copy p{margin-bottom:21.6px}
.about-copy strong{font-weight:700}

.rule{position:absolute;left:0;top:711px;width:1200px;height:6px;background:var(--orange)}
.site-footer{position:absolute;left:0;top:717px;width:1200px;height:118px;background:var(--footer-bg)}
.footer-info{position:absolute;left:189px;top:25px;font-size:12px;line-height:17.5px;color:var(--footer-text)}
.footer-brand{position:absolute;left:935px;top:40px;display:flex;align-items:center;gap:8px}
.footer-brand .brand-dot{width:22px;height:22px;background:var(--grey)}
.footer-brand .brand-name{font-size:14px;color:var(--grey)}
</style>
</head>
<body>
<header class="site-header">
  <div class="brand">
    <span class="brand-dot"></span>
    <span class="brand-name">Mesa Verda Lighting</span>
  </div>
  <div class="contact-bar">
    <span class="contact-line">Alta Vista, TX 79000, Phone: 555-010-0370</span>
    <span class="social" aria-label="Social link"></span>
    <span class="social" aria-label="Social link"></span>
    <span class="social" aria-label="Social link"></span>
  </div>
  <nav class="main-nav">
    <a class="nav-item">Home</a>
    <a class="nav-item is-active">AboutLine</a>
    <a class="nav-item">CardServices</a>
    <a class="nav-item">Territory</a>
    <a class="nav-item">MapPhoto</a>
    <a class="nav-item">Gallery</a>
    <a class="nav-item">Contact</a>
  </nav>
</header>

<section class="hero-photo" role="img" aria-label="Team of five smiling staff standing with arms crossed in a lighting warehouse">
  <h1 class="hero-title">About us</h1>
</section>
<div class="shade"></div>

<article class="about-copy">
  <p><strong>Mesa Verda Lighting</strong> started operations in 1996 to help develop the border region with cutting edge lighting solutions to maximize design efficiencies. With unparalleled integrity, we continue to provide our clients and manufacturing partners with impactful results.</p>
  <p>We truly believe in enjoying a mutually beneficial partnership with our stakeholders.</p>
  <p><strong>Mesa Verda Lighting’s</strong> expertise excels in Design and Technical applications for energy saving, sustainability, and green building initiatives, to include Carbon Footprint and Return on Investment (ROI) analysis.</p>
  <p>Our experiences lie in a variety of architectural, commercial, industrial, institutional, and residential lighting projects as well as controls projects.</p>
  <p>We are an integrated team of dedicated professionals ready to support your projects in English and Spanish.</p>
</article>

<div class="rule"></div>
<footer class="site-footer">
  <div class="footer-info">
    Mesa Verda Lighting &amp; Design<br>
    LED Lighting Experts<br>
    1420 Cedar Ridge Dr , Alta Vista Texas United States 79000<br>
    © 2016 Mesa Verda Lighting &amp; Design. All Rights Reserved.
  </div>
  <div class="footer-brand">
    <span class="brand-dot"></span>
    <span class="brand-name">Mesa Verda Lighting</span>
  </div>
</footer>
</body>
</html>
```